New Template design for Website in Wordpress

We are interested in changing our website look at www.cargolinx.com -We also are very interested in Have it done in Wordpress in which we are understanding the search engines are liking a bit more. The website we would want to try working with on this is www.cargolinx.com. We look forward to seeing the different design ideas please just make sure they are in wordpress! Thanks, Marlen

Reason: need more design idea..... We would still like to use our pictures off our site since we paid for them so keep that in mind as well as we would still want the rotating pictures in the head of the page but not in Flash.

```html
<!DOCTYPE html>
<html lang="en">
<head>
<meta charset="utf-8">
<title>Cargolinx — Logistics Freight Company</title>
<link href="https://fonts.googleapis.com/css2?family=Open+Sans:wght@400;600;700&family=Oswald:wght@500;600&display=swap" rel="stylesheet">
<style>
:root{
  --ink:#1c1c1c;
  --ink-soft:#2a2a2a;
  --red:#d0342c;
  --text:#555;
  --muted:#8a8a8a;
  --line:#dcdcdc;
  --paper:#ffffff;
  --footer:#1a1a1a;
  --footer-text:#9a9a9a;
}
*{box-sizing:border-box;margin:0;padding:0}
html,body{width:880px;height:1200px;overflow:hidden}
body{font-family:"Open Sans",Arial,sans-serif;background:var(--paper);color:var(--text);font-size:11px;line-height:1.5}
.site-header{height:60px;background:var(--ink);display:flex;justify-content:space-between;padding:0 70px;position:relative}
.brand{padding-top:10px}
.brand-name{font-family:"Oswald",Arial,sans-serif;font-weight:600;font-size:22px;color:#fff;letter-spacing:1px;line-height:1}
.brand-tag{font-size:8px;color:var(--muted);letter-spacing:1px;text-transform:uppercase}
.header-right{text-align:right;padding-top:6px}
.call{color:#fff;font-weight:700;font-size:12px}
.call span{color:var(--red)}
.main-nav{display:flex;gap:2px;margin-top:14px}
.main-nav a{color:#ddd;text-decoration:none;font-size:9px;font-weight:600;text-transform:uppercase;padding:5px 8px}
.main-nav a.active{background:var(--red);color:#fff}
.hero{height:210px;position:relative;background:linear-gradient(160deg,#7f98ad 0%,#5b6f82 35%,#8a4a3a 62%,#3f4a55 100%)}
.hero-caption{position:absolute;left:70px;top:52px;width:300px;color:#fff}
.hero-caption h1{font-family:"Oswald",Arial,sans-serif;font-weight:500;font-size:30px;line-height:1.1;margin-bottom:8px}
.hero-caption p{font-size:10px;margin-bottom:10px}
.btn{display:inline-block;background:var(--red);color:#fff;font-size:8px;font-weight:700;text-transform:uppercase;padding:4px 9px;text-decoration:none}
.btn-dark{background:var(--ink)}
.hero-arrow{position:absolute;top:92px;width:22px;height:26px;background:rgba(0,0,0,.45)}
.hero-arrow.prev{left:0}.hero-arrow.next{right:0}
.services{display:flex;gap:40px;padding:32px 70px 0}
.service{flex:1}
.service-photo{height:130px;margin-bottom:16px}
.p-ship{background:linear-gradient(180deg,#9cc3e0,#2f6aa0 60%,#1f3e66)}
.p-truck{background:linear-gradient(180deg,#bcd6ec,#6f8fb0 55%,#4d4f57)}
.p-cargo{background:linear-gradient(180deg,#c6d7e6,#9aa7b4 50%,#5c6672)}
.service h2{font-family:"Open Sans",Arial,sans-serif;font-size:15px;font-weight:700;color:var(--ink);margin-bottom:6px}
.service p{font-size:10px;margin-bottom:12px;height:62px}
.services-rule{margin:26px 70px 0;border-top:1px solid var(--line)}
.cta{margin:120px 70px 0;height:82px;background:var(--ink-soft);display:flex;align-items:center;justify-content:space-between;padding:0 30px}
.cta p{color:#eee;font-size:11px;font-weight:600;width:430px}
.cta .btn{font-size:10px;padding:9px 16px}
.welcome{display:flex;gap:40px;padding:34px 70px 0;height:258px}
.welcome-text{flex:1}
.welcome-text h2{font-size:17px;font-weight:400;color:var(--ink);margin-bottom:10px}
.welcome-text p{font-size:10px}
.social-box{width:190px;height:176px;border:1px solid var(--line);padding:10px}
.social-head{display:flex;gap:8px;align-items:center;margin-bottom:8px}
.social-mark{width:30px;height:30px;background:var(--red)}
.social-name{font-size:11px;font-weight:700;color:var(--ink)}
.social-sub{font-size:8px;color:var(--muted)}
.fans{display:grid;grid-template-columns:repeat(5,1fr);gap:5px;margin-top:6px}
.fans span{height:26px;background:#d9dde2}
.site-footer{background:var(--footer);height:122px;padding:18px 70px 0;display:flex;gap:24px}
.footer-col{flex:1}
.footer-col h3{font-size:10px;color:#fff;font-weight:700;margin-bottom:6px}
.footer-col ul{list-style:none}
.footer-col li{font-size:8.5px;color:var(--footer-text);line-height:1.55}
.footer-contact h3{font-size:12px}
.footer-contact p{font-size:8.5px;color:var(--footer-text)}
.bottom-bar{background:#111;height:28px;padding:0 70px;display:flex;align-items:center;justify-content:space-between;font-size:8px;color:#777}
</style>
</head>
<body>
<header class="site-header">
  <div class="brand">
    <div class="brand-name">CARGOLINX</div>
    <div class="brand-tag">a logistics freight company</div>
  </div>
  <div class="header-right">
    <div class="call">CALL: <span>(555) 014-2270</span></div>
    <nav class="main-nav">
      <a class="active" href="#">Home</a><a href="#">About Us</a><a href="#">Our Services</a><a href="#">Contact Us</a><a href="#">Get Instant Quote</a>
    </nav>
  </div>
</header>

<section class="hero" role="img" aria-label="Photo of a container port with a cargo ship and stacked shipping containers">
  <div class="hero-caption">
    <h1>Ocean Shipping<br>Services</h1>
    <p>Fast ocean freight across the globe with careful handling and on-time delivery for every load.</p>
    <a class="btn" href="#">Read more</a>
  </div>
  <svg class="hero-arrow prev" viewBox="0 0 22 26"><path d="M13 8l-5 5 5 5" stroke="#fff" stroke-width="2" fill="none"/></svg>
  <svg class="hero-arrow next" viewBox="0 0 22 26"><path d="M9 8l5 5-5 5" stroke="#fff" stroke-width="2" fill="none"/></svg>
</section>

<section class="services">
  <article class="service">
    <div class="service-photo p-ship" role="img" aria-label="Photo of a loaded container ship at sea"></div>
    <h2>Freight Services</h2>
    <p>Our freight team moves cargo of every size by land, sea and air. We plan each route with care and keep you informed from pickup to final delivery.</p>
    <a class="btn btn-dark" href="#">Read more</a>
  </article>
  <article class="service">
    <div class="service-photo p-truck" role="img" aria-label="Photo of a semi truck on the highway"></div>
    <h2>Trucking Services</h2>
    <p>Our trucking network links you with trusted carriers nationwide. Full loads, partial loads and expedited runs are handled quickly and at fair rates.</p>
    <a class="btn btn-dark" href="#">Read more</a>
  </article>
  <article class="service">
    <div class="service-photo p-cargo" role="img" aria-label="Photo of oversized special cargo being loaded"></div>
    <h2>Special Cargo</h2>
    <p>We move oversized, heavy and delicate cargo with the right equipment, permits and escorts so every special shipment arrives safe and sound.</p>
    <a class="btn btn-dark" href="#">Read more</a>
  </article>
</section>
<div class="services-rule"></div>

<section class="cta">
  <p>Get your freight quote online now or call (555) 014-2270 and let one of the top carriers in the country handle your business today.</p>
  <a class="btn" href="#">Get Instant Quote</a>
</section>

<section class="welcome">
  <div class="welcome-text">
    <h2>Welcome to Cargolinx</h2>
    <p>Welcome to Cargolinx, your partner for freight, trucking and ocean shipping. For years we have helped businesses of every size move goods across the country and around the world. Our team compares rates from trusted carriers, books the best option and tracks each load until it arrives. Call us or request a quote online to get started today.</p>
  </div>
  <aside class="social-box">
    <div class="social-head">
      <div class="social-mark"></div>
      <div><div class="social-name">Cargolinx</div><div class="social-sub">Follow our page</div></div>
    </div>
    <div class="social-sub">248 people follow Cargolinx</div>
    <div class="fans"><span></span><span></span><span></span><span></span><span></span><span></span><span></span><span></span><span></span><span></span></div>
  </aside>
</section>

<footer class="site-footer">
  <div class="footer-col">
    <h3>Worldwide Freight Services</h3>
    <ul><li>Worldwide Freight Quotes</li><li>Air Freight Services</li><li>Ocean Freight Services</li><li>Customs Clearance</li><li>Import and Export</li></ul>
  </div>
  <div class="footer-col">
    <h3>Freight - Trucking Service</h3>
    <ul><li>Heavy Equipment Hauling</li><li>LTL Freight Transport</li><li>Flatbed Transport</li><li>Expedited Transport</li><li>Dry Van Transport</li></ul>
  </div>
  <div class="footer-col">
    <h3>Ocean Shipping Services</h3>
    <ul><li>Container Shipping</li><li>Roll On Roll Off</li><li>Breakbulk Cargo</li><li>Project Cargo</li><li>Port to Port Service</li></ul>
  </div>
  <div class="footer-col footer-contact">
    <h3>CONTACT US</h3>
    <p>Call our freight experts at (555) 014-2270 or send us a note and we will reply within one business day.</p>
  </div>
</footer>
<div class="bottom-bar"><span>Copyright 2014 Cargolinx. All rights reserved.</span><span>Privacy Policy</span></div>
</body>
</html>
```